Design for BusinessCard and Letterhead

Hello,

i need the design for Business Card and for letterhead

First of all some general information about the design:
Attached you'll find my company's logo. It should be both on the BusinessCard and on the stationery.
You'll also find a Billdboard design, and the design of our cars. This is my Homepage: [login to view URL] - If you look at these files and on the Homepage you know our' companies colors and what I like.
On my homepage on the Billboard and also on the Cars you find a Photo of a girl. I don't want that girl neither on the BusinessCrads nor on the stationery. In fact I also don't want the other fotos from the billboard on the Bausinesscards and ond the stationery.

The winner has also to provide the used fonts to me.

The Business Cards:
The Business Cards should be double Sided. The dimensions are 85 x 55 mm (milimeters)
It should contain the followog:
The Logo, the Persons name & his position in the company, The COpanies name, contact Information and the services

To the letterhead:
The Dimensions of the Statinery are: 210 × 297 mm
The Stationery should contain:
The Logo, The COpanies name, contact Information, services and the legal Stuff
Here are some general Information about the Letterhead.
1) The contact Information must be placed on the right upper side of the sheet. I want all the inforation i provided on the sheet, not only part of them.
2) The Services have to be more vissbile. The must be bigger, so that everyone knows that services we provide. That is very important.

Here are the needed information:
The Persons Name: Tovmo Quenlaxx
The Persons Positions in the COmpany: Geschäftsführer
The Name of the Company: Quenla Maler-GmbH
Contact Information:
Adress: Folkengasse 27/5, 1160 Wien
Mobile Phone: +43 664 555 12 34
Fon: +43 1 555 12 34
Fax: +43 1 555 12 35

Homepage: [login to view URL]
Mail: office@quenla-maler.example

Our Services:
Malerei
Anstrich
Fassaden
Tapeten
Wanddekorationen
Parkettböden

Legal Informations (only for the stationery):
Bankverbindung: Donaumark Kreditbank Noe - Wien
IBAN: AT00 5555 6666 7777 8888
BIC: QZMKATVV
Firmenbuch-Nr.: 555555x HG WIen
UID-Nr.: 555555555
DG-Nr.: 55556666
Gerichtsstand: Wien

If you have any questions don't hesitate to ask.

Regards,
Tovmo

```html
<!DOCTYPE html>
<html lang="de">
<head>
<meta charset="utf-8">
<title>Quenla Maler-GmbH – Visitenkarte</title>
<link rel="stylesheet" href="https://fonts.googleapis.com/css2?family=Fira+Sans:wght@400;500;700&display=swap">
<style>
  :root {
    --red: #e2231a;
    --ink: #2b2b2b;
    --black: #141414;
    --grey: #6b6b6b;
    --paper: #ffffff;
    --stage: #d9d9d9;
  }
  html, body {
    margin: 0;
    width: 1200px;
    height: 900px;
    overflow: hidden;
    background: var(--stage);
    font-family: "Fira Sans", Arial, sans-serif;
    color: var(--ink);
  }
  .sheet {
    width: 1200px;
    height: 900px;
    display: flex;
    align-items: center;
    justify-content: center;
    gap: 40px;
  }
  .card {
    position: relative;
    width: 540px;
    height: 350px;
    background: var(--paper);
    box-shadow: 0 6px 18px rgba(0,0,0,.25);
    overflow: hidden;
  }
  .card-edge {
    position: absolute;
    inset: 0;
    width: 540px;
    height: 350px;
  }

  /* Back side: brand block and services */
  .brand-block {
    position: absolute;
    left: 60px;
    top: 62px;
    width: 170px;
    text-align: center;
  }
  .brand-square {
    width: 150px;
    height: 150px;
    margin: 0 auto 12px;
    background: var(--red);
    border-radius: 14px;
  }
  .brand-name {
    font-weight: 700;
    font-size: 30px;
    color: var(--red);
    line-height: 1;
  }
  .services {
    position: absolute;
    left: 260px;
    top: 62px;
    margin: 0;
    padding: 0;
    list-style: none;
  }
  .services li {
    display: flex;
    align-items: center;
    gap: 9px;
    font-size: 25px;
    line-height: 35px;
    color: var(--ink);
  }
  .services li::before {
    content: "";
    width: 15px;
    height: 15px;
    background: var(--red);
    border-radius: 2px;
    flex: none;
  }

  /* Front side: identity and contact */
  .identity {
    position: absolute;
    right: 34px;
    top: 26px;
    display: flex;
    align-items: center;
    gap: 10px;
  }
  .identity-square {
    width: 46px;
    height: 46px;
    background: var(--red);
    border-radius: 6px;
  }
  .identity-name {
    font-weight: 700;
    font-size: 46px;
    line-height: 1;
    color: var(--ink);
  }
  .identity-legal {
    position: absolute;
    right: 36px;
    top: 80px;
    font-size: 12px;
    font-weight: 500;
    color: var(--grey);
  }
  .person {
    position: absolute;
    left: 58px;
    top: 112px;
  }
  .person-name {
    font-weight: 700;
    font-size: 20px;
    margin: 0;
  }
  .person-role {
    font-size: 14px;
    color: var(--red);
    margin: 2px 0 0;
  }
  .rule {
    position: absolute;
    left: 58px;
    right: 34px;
    top: 168px;
    height: 1px;
    background: var(--red);
  }
  .phones {
    position: absolute;
    left: 58px;
    top: 178px;
    margin: 0;
    padding: 0;
    list-style: none;
    font-size: 12.5px;
    line-height: 19px;
  }
  .phones li, .contact li {
    display: flex;
    align-items: center;
    gap: 7px;
  }
  .icon {
    width: 12px;
    height: 12px;
    fill: var(--grey);
    flex: none;
  }
  .contact {
    position: absolute;
    right: 34px;
    bottom: 30px;
    margin: 0;
    padding: 0 12px 0 0;
    list-style: none;
    font-size: 13px;
    line-height: 20px;
    border-right: 1px solid var(--red);
  }
  .contact li { justify-content: flex-end; }
  .contact .icon { order: 2; }
</style>
</head>
<body>
<main class="sheet">

  <section class="card card-back" aria-label="Visitenkarte Rückseite">
    <svg class="card-edge" viewBox="0 0 540 350" aria-hidden="true">
      <polygon points="0,88 24,112 24,350 0,350" fill="var(--black)"/>
      <polygon points="0,70 24,94 24,112 0,88" fill="var(--red)"/>
      <polygon points="488,0 540,0 540,70" fill="var(--black)"/>
      <polygon points="470,0 488,0 540,70 540,94" fill="var(--red)"/>
    </svg>
    <div class="brand-block">
      <div class="brand-square"></div>
      <div class="brand-name">Quenla</div>
    </div>
    <ul class="services">
      <li>Malerei</li>
      <li>Anstrich</li>
      <li>Fassaden</li>
      <li>Tapeten</li>
      <li>Wanddekorationen</li>
      <li>Parkettböden</li>
    </ul>
  </section>

  <section class="card card-front" aria-label="Visitenkarte Vorderseite">
    <svg class="card-edge" viewBox="0 0 540 350" aria-hidden="true">
      <polygon points="0,90 22,112 22,300 0,320" fill="var(--red)"/>
      <polygon points="0,320 22,300 22,350 0,350" fill="var(--black)"/>
    </svg>
    <div class="identity">
      <div class="identity-square"></div>
      <div class="identity-name">Quenla</div>
    </div>
    <div class="identity-legal">Maler-GmbH</div>

    <div class="person">
      <p class="person-name">Tovmo Quenlaxx</p>
      <p class="person-role">Managing Director</p>
    </div>
    <div class="rule"></div>

    <ul class="phones">
      <li><svg class="icon" viewBox="0 0 12 12"><rect x="3" y="0.5" width="6" height="11" rx="1"/></svg>+43 664 555 12 34</li>
      <li><svg class="icon" viewBox="0 0 12 12"><path d="M2 1h3l1 3-2 1a7 7 0 0 0 3 3l1-2 3 1v3a1 1 0 0 1-1 1A10 10 0 0 1 1 2a1 1 0 0 1 1-1z"/></svg>+43 1 555 12 34</li>
      <li><svg class="icon" viewBox="0 0 12 12"><rect x="3" y="0.5" width="6" height="4"/><rect x="0.5" y="4" width="11" height="5" rx="1"/><rect x="3" y="8" width="6" height="3.5"/></svg>+43 1 555 12 35</li>
    </ul>

    <ul class="contact">
      <li><svg class="icon" viewBox="0 0 12 12"><path d="M0.5 2h11v8h-11z M1 2.5l5 4 5-4" /></svg>office@quenla-maler.example</li>
      <li><svg class="icon" viewBox="0 0 12 12"><circle cx="6" cy="6" r="5.5"/></svg>www.quenla-maler.example</li>
      <li><svg class="icon" viewBox="0 0 12 12"><path d="M6 0a4 4 0 0 1 4 4c0 3-4 8-4 8S2 7 2 4a4 4 0 0 1 4-4z"/></svg>Folkengasse 27/5, 1160 Vienna</li>
    </ul>
  </section>

</main>
</body>
</html>
```